Lower Cost Storage Scheme Email marketing campaign for Corvel Energy

Design a visually engaging and professional marketing email to promote the upcoming Federal Government Battery Subsidy to our existing solar clients, encouraging them to install a battery system now to maximise savings. email content example "Subject: ⚡ Federal Government Battery Subsidy is Coming – Maximise Your Solar Savings

Body:
Hi [First Name],

Great news! With the federal election now decided, the Federal Government’s Home Battery Subsidy Program is officially on the way.

While the scheme hasn’t formally launched yet, it's guaranteed—and like the solar rebate before it, the subsidy reduces each year, so the earlier you install, the more you’ll save.

Crucially, the subsidy is only available once per household, so it makes sense to install a system that fully meets your home's battery needs right from the start.

Why add a battery to your existing solar system now?
✅ Store your excess solar energy instead of sending it back to the grid for low feed-in tariffs
✅ Use your stored solar power at night, when electricity prices are highest (typically 5–8pm)
✅ Slash your power bills and avoid rising time-of-use charges
✅ Protect your home from power outages
✅ Increase your self-sufficiency and long-term energy security

If you’ve already installed solar with us, now is the ideal time to complete your setup with a battery system designed to maximise your return—and take full advantage of this one-off federal subsidy.

Call us today or reply to this email to secure your spot and beat the rush.

Let your solar work smarter for your home,
The Corvel Energy Team"

Target Market(s)

Content: We’ve provided the copy (see attached or below). The key points to emphasise in the design are: The urgency (subsidy winds down each year, limited to one per household). The benefits of installing a battery now, including energy savings, time-of-use charge avoidance, and self-sufficiency. Call to action: “Call us today or reply to this email to secure your spot and beat the rush.”

Industry/Entity Type

Renewable Energy

Colors
0054AA
0677BA
7BADD7
CADEEF
E8F1F8
EB3D1F
EC4F4E
F09395
F8D3D4
FCEDEE

Requirements
Must have
• Clean, modern, and trustworthy – aligned with Corvel Energy branding. Bold headers and icons to make key points stand out. Include visual elements such as: A solar battery image Infographic or icon-style section showing key battery benefits (e.g. bill savings, backup power, self-consumption) Highlighted call-to-action button (“Secure My Battery Now” or “Beat the Rush”)
Nice to have
• I would like to have our company imagery (Corvel Energy) alongside the battery brands we offer being Velto, QMP, Brimlite and TervoPWR
Should not have
• Unsure

```html
<!DOCTYPE html>
<html lang="en">
<head>
<meta charset="utf-8">
<title>Corvel Energy – Battery Subsidy Email</title>
<link href="https://fonts.googleapis.com/css2?family=Barlow:wght@500;600;700&family=Barlow+Semi+Condensed:wght@600;700&display=swap" rel="stylesheet">
<style>
  :root {
    --page-bg: #f4f5f7;
    --card-bg: #ffffff;
    --navy: #123a6a;
    --ink: #1f2a37;
    --brand-blue: #1f6fc0;
    --hero-bg: #e6f2fc;
    --orange: #ff7a00;
    --orange-badge: #ff7a12;
    --peach: #fdeee2;
    --panel-blue-top: #cfe3fa;
    --panel-blue-bottom: #e8f1fb;
    --rule: #dfe8f1;
    --brand-grey: #7a7f86;
  }
  * { margin: 0; padding: 0; box-sizing: border-box; }
  html, body { width: 799px; height: 1200px; overflow: hidden; }
  body {
    background: var(--page-bg);
    font-family: "Barlow", Arial, sans-serif;
    color: var(--ink);
    position: relative;
  }
  .email-card {
    position: absolute; left: 43px; top: 30px; width: 713px; height: 1140px;
    background: var(--card-bg);
    box-shadow: 0 2px 14px rgba(20, 40, 70, 0.08);
  }
  .brand-header {
    position: absolute; left: 59px; top: 40px;
    display: flex; align-items: center; gap: 10px;
  }
  .brand-dot { width: 30px; height: 30px; border-radius: 50%; background: var(--orange); }
  .brand-name {
    font-family: "Barlow", sans-serif; font-weight: 700; font-size: 34px;
    color: var(--navy); letter-spacing: 0.5px;
  }
  .hero-band {
    position: absolute; left: 0; top: 107px; width: 713px; height: 189px;
    background: var(--hero-bg);
  }
  .hero-title {
    position: absolute; left: 59px; top: 30px; width: 640px;
    font-family: "Barlow Semi Condensed", sans-serif; font-weight: 700;
    font-size: 41px; line-height: 44px; color: var(--navy);
    text-transform: uppercase; white-space: nowrap;
  }
  .hero-title svg { vertical-align: -3px; margin: 0 10px 0 8px; }
  .greeting {
    position: absolute; left: 59px; top: 325px;
    font-weight: 600; font-size: 19px; color: var(--ink);
  }
  .urgency-badge {
    position: absolute; left: 59px; top: 373px; width: 245px; height: 35px;
    background: var(--orange-badge); border-radius: 6px;
    color: #fff; font-family: "Barlow Semi Condensed", sans-serif; font-weight: 600;
    font-size: 17px; line-height: 35px; text-align: center; text-transform: uppercase;
  }
  .intro-copy {
    position: absolute; left: 59px; top: 428px; width: 370px;
    font-weight: 500; font-size: 17px; line-height: 26px; color: var(--ink);
  }
  .benefits-heading {
    position: absolute; left: 59px; top: 526px;
    font-weight: 600; font-size: 19px; color: var(--ink); line-height: 26px;
  }
  .benefits-heading small {
    display: block; font-size: 16px; font-weight: 600; text-transform: uppercase;
  }
  .benefit-list { position: absolute; left: 59px; top: 591px; list-style: none; }
  .benefit-item {
    display: flex; align-items: center; height: 46.5px;
    font-weight: 600; font-size: 18.5px; color: var(--ink);
  }
  .benefit-icon { width: 36px; height: 36px; margin-right: 19px; flex: none; }
  .section-rule {
    position: absolute; left: 59px; top: 841px; width: 339px; height: 1px; background: var(--rule);
  }
  .closing-line {
    position: absolute; left: 59px; top: 866px;
    font-weight: 600; font-size: 23px; color: var(--navy); text-transform: uppercase; letter-spacing: 0.2px;
  }
  .battery-visual {
    position: absolute; left: 433px; top: 374px; width: 224px; height: 333px;
    border-radius: 8px; border: 1px solid #cfe0f3;
    background: linear-gradient(160deg, var(--panel-blue-top), var(--panel-blue-bottom) 70%, #f6f9fd);
  }
  .subsidy-note {
    position: absolute; left: 433px; top: 727px; width: 224px; height: 183px;
    background: var(--peach); border-radius: 8px;
    padding: 22px 12px 0 23px;
    font-weight: 500; font-size: 17px; line-height: 25px; color: var(--ink);
  }
  .cta-button {
    position: absolute; left: 59px; top: 927px; width: 597px; height: 60px;
    background: var(--orange); border-radius: 5px;
    color: #fff; text-align: center; line-height: 60px; text-decoration: none;
    font-family: "Barlow Semi Condensed", sans-serif; font-weight: 700; font-size: 24px; text-transform: uppercase;
  }
  .footer-rule {
    position: absolute; left: 59px; top: 1017px; width: 597px; height: 1px; background: var(--rule);
  }
  .partner-brands {
    position: absolute; left: 59px; top: 1045px; width: 597px; height: 32px;
  }
  .partner-name {
    position: absolute; top: 0;
    font-weight: 600; font-size: 24px; color: var(--brand-grey); letter-spacing: 1px;
  }
  .partner-velto { left: 7px; }
  .partner-qmp { left: 136px; }
  .partner-brimlite { left: 241px; }
  .partner-tervo { left: 462px; }
</style>
</head>
<body>
  <main class="email-card">
    <header class="brand-header">
      <span class="brand-dot"></span>
      <span class="brand-name">CORVEL ENERGY</span>
    </header>

    <section class="hero-band">
      <h1 class="hero-title">
        <svg width="28" height="36" viewBox="0 0 30 36" aria-hidden="true"><path d="M18 1 4 21h10l-3 14 15-21H16z" fill="var(--orange)"/></svg>Federal Government<br>Battery Subsidy is coming –<br>Maximise your solar savings
      </h1>
    </section>

    <p class="greeting">Hi (First Name),</p>
    <div class="urgency-badge">New subsidy – Act fast</div>
    <p class="intro-copy">Great news! With the federal election now decided, the Federal Government’s Home Battery Subsidy Program is officially on the way.</p>

    <h2 class="benefits-heading">Why add a battery to your existing<small>Solar system now?</small></h2>

    <ul class="benefit-list">
      <li class="benefit-item">
        <svg class="benefit-icon" viewBox="0 0 36 36" fill="none" stroke="var(--brand-blue)" stroke-width="2.4" stroke-linejoin="round" stroke-linecap="round"><path d="M4 17 18 4l14 13M8 14v18h20V14"/><path d="m12 22 4 4 8-8"/></svg>
        Store excess solar power
      </li>
      <li class="benefit-item">
        <svg class="benefit-icon" viewBox="0 0 36 36" fill="none" stroke="var(--brand-blue)" stroke-width="2.4" stroke-linecap="round"><path d="M15 6a12 12 0 1 0 15 15A10 10 0 0 1 15 6z"/><path d="m27 30 4-4"/></svg>
        Use solar at night, cut tariff charges
      </li>
      <li class="benefit-item">
        <svg class="benefit-icon" viewBox="0 0 36 36" fill="none" stroke="var(--brand-blue)" stroke-width="2.4" stroke-linejoin="round"><path d="M6 32h26M8 32V22h5v10M16 32V16h5v16M24 32V8h5v24"/></svg>
        Lower your energy bills
      </li>
      <li class="benefit-item">
        <svg class="benefit-icon" viewBox="0 0 36 36" fill="none" stroke="var(--brand-blue)" stroke-width="2.4" stroke-linejoin="round"><path d="M18 3 5 8v9c0 8 6 13 13 16 7-3 13-8 13-16V8z"/><path d="m20 10-6 9h5l-2 7 6-9h-5z"/></svg>
        Backup during power outages
      </li>
      <li class="benefit-item">
        <svg class="benefit-icon" viewBox="0 0 36 36" fill="none" stroke="var(--brand-blue)" stroke-width="2.4" stroke-linecap="round"><circle cx="18" cy="18" r="14"/><path d="m11 19 5 4 9-10"/></svg>
        Energy independence
      </li>
    </ul>

    <div class="section-rule"></div>
    <p class="closing-line">Let your solar work smarter</p>

    <div class="battery-visual" role="img" aria-label="Product photo of a white home energy storage battery unit"></div>

    <aside class="subsidy-note">The subsidy reduces each year and is limited to one per household–installing a battery now ensures you don’t miss out!</aside>

    <a class="cta-button" href="#">Beat the rush – Reserve my battery</a>

    <div class="footer-rule"></div>
    <nav class="partner-brands" aria-label="Battery brands we offer">
      <span class="partner-name partner-velto">VELTO</span>
      <span class="partner-name partner-qmp">QMP</span>
      <span class="partner-name partner-brimlite">BRIMLITE</span>
      <span class="partner-name partner-tervo">TervoPWR</span>
    </nav>
  </main>
</body>
</html>
```